Dental Office Looking for Modern, simple business cards

We just acquired our logo. Now we would like to make business cards. We are a dental office with two doctors. We are husband and wife and have a small boutique dental practice in a small town. We love our patients and they are always asking us to give our business cards to their friends. Please help us make business cards :-)

Target Market(s)

30-60 yr old

Industry/Entity Type

Dental Clinic

Contact Information for Business Card

Birch Hollow Dental P.C.
Family and Cosmetic Dentistry
4827 Dunmore Rd. Schenectady NY 12309
Tel: 518 642 8817 Fax: 518 642 8830

Dr. Tomas K. Elridge DDS
Dr. Marisol Anne Whitby DDS

Font styles to use
Serif
Sans Serif

Requirements
Must have
• Simple clean design, modern, colorful. Should incorporate the logo.
Nice to have
• dental imagery ( teeth, smile, etc ...).

```html
<!DOCTYPE html>
<html lang="en">
<head>
<meta charset="utf-8">
<title>Birch Hollow Dental – Business Cards</title>
<link rel="stylesheet" href="https://fonts.googleapis.com/css2?family=Open+Sans:wght@400;700&display=swap">
<style>
  :root {
    --brand-blue: #1075bf;
    --swoosh-grey: #85868a;
    --text-grey: #5d5e62;
    --rule-grey: #c9cacc;
    --card-white: #ffffff;
    --backdrop: #e6e8eb;
  }
  html, body {
    margin: 0;
    padding: 0;
    width: 1200px;
    height: 900px;
    overflow: hidden;
    background: var(--backdrop);
    font-family: "Open Sans", Arial, sans-serif;
  }
  .canvas {
    position: relative;
    width: 1200px;
    height: 900px;
  }
  .card {
    position: absolute;
    left: 320px;
    width: 560px;
    height: 320px;
    border-radius: 22px;
    overflow: hidden;
    box-shadow: 0 6px 18px rgba(0,0,0,0.18);
  }
  .card--front {
    top: 90px;
    background: var(--brand-blue);
    display: flex;
    align-items: center;
    justify-content: center;
  }
  .front-name {
    color: var(--card-white);
    font-weight: 700;
    font-size: 40px;
    letter-spacing: 2px;
    text-transform: uppercase;
  }
  .card--back {
    top: 490px;
    background: var(--card-white);
  }
  .back-art {
    position: absolute;
    inset: 0;
  }
  .doctors {
    position: absolute;
    left: 34px;
    top: 108px;
    margin: 0;
    color: var(--brand-blue);
    font-weight: 700;
    font-size: 15px;
    line-height: 26px;
  }
  .contact-rule {
    position: absolute;
    left: 30px;
    top: 176px;
    width: 500px;
    height: 1px;
    background: linear-gradient(to right, var(--brand-blue) 0 42%, var(--rule-grey) 42% 100%);
  }
  .phones {
    position: absolute;
    left: 30px;
    top: 190px;
    margin: 0;
    padding: 0;
    list-style: none;
    color: var(--text-grey);
    font-size: 15px;
    line-height: 26px;
  }
  .phones li {
    display: flex;
    align-items: center;
    gap: 10px;
  }
  .phones svg {
    width: 12px;
    height: 12px;
    fill: var(--brand-blue);
  }
  .practice {
    position: absolute;
    right: 34px;
    top: 90px;
    text-align: right;
  }
  .practice-mark {
    color: var(--text-grey);
    font-weight: 700;
    font-size: 24px;
    line-height: 30px;
    letter-spacing: 1px;
    text-transform: uppercase;
    margin: 0 0 4px;
  }
  .practice-name {
    color: var(--brand-blue);
    font-weight: 700;
    font-size: 14px;
    line-height: 20px;
    margin: 0;
  }
  .practice-tagline {
    color: var(--text-grey);
    font-size: 13px;
    line-height: 18px;
    margin: 0;
  }
  .address {
    position: absolute;
    right: 34px;
    top: 248px;
    margin: 0;
    text-align: right;
    color: var(--text-grey);
    font-size: 15px;
    line-height: 22px;
    font-style: normal;
  }
</style>
</head>
<body>
<main class="canvas">

  <section class="card card--front" aria-label="Card front">
    <span class="front-name">Birch Hollow Dental</span>
  </section>

  <section class="card card--back" aria-label="Card back">
    <svg class="back-art" viewBox="0 0 560 320" aria-hidden="true">
      <path d="M0,0 H560 V42 Q300,60 0,76 Z" fill="var(--brand-blue)"/>
      <path d="M70,78 Q320,66 560,46 V62 Q320,74 70,78 Z" fill="var(--swoosh-grey)"/>
    </svg>

    <p class="doctors">Dr. Tomas K. Elridge DDS<br>Dr. Marisol Anne Whitby DDS</p>
    <div class="contact-rule"></div>

    <ul class="phones">
      <li>
        <svg viewBox="0 0 24 24"><path d="M6.6 10.8a15 15 0 0 0 6.6 6.6l2.2-2.2c.3-.3.7-.4 1-.2 1.1.4 2.3.6 3.6.6.6 0 1 .4 1 1V20c0 .6-.4 1-1 1A17 17 0 0 1 3 4c0-.6.4-1 1-1h3.5c.6 0 1 .4 1 1 0 1.3.2 2.5.6 3.6.1.3 0 .7-.2 1z"/></svg>
        518 642 8817
      </li>
      <li>
        <svg viewBox="0 0 24 24"><path d="M6 2h12v6H6zM4 9h16a2 2 0 0 1 2 2v6h-4v5H6v-5H2v-6a2 2 0 0 1 2-2zm4 8v3h8v-3z"/></svg>
        518 642 8830
      </li>
    </ul>

    <div class="practice">
      <p class="practice-mark">Birch Hollow Dental</p>
      <p class="practice-name">BIRCH HOLLOW DENTAL P.C.</p>
      <p class="practice-tagline">Family and Cosmetic Dentistry</p>
    </div>

    <address class="address">4827 Dunmore Rd. Schenectady<br>NY 12309</address>
  </section>

</main>
</body>
</html>
```